Pecan Ridge Paving. Chip Seal Done Right

I need my card to have all my basic information on it. Keep it simple. Include web site, phone number and email address. Include phrase Chip Seal Done Right or Pecan Ridge’s Top Paving Company. Keep card simple. Include color and logo. Put all contact info on card. Make card simple and not complicated.

Here is infuriation yo out in business card

Dale R. Whitmore
830.555.0173 cell phone
Dalewhitmore7@mailbarn.net
www.pecanridgepaving.net

Target Market(s)

Hill Country Texas USA

Industry/Entity Type

Road chip seal

Contact Information for Business Card

We chip seal roads for ranches and property owners

Font styles to use
Serif
Sans Serif
Decorative
Script

Colors
0054AA
0677BA
7BADD7
CADEEF
E8F1F8
EB3D1F
EC4F4E
F09395
F8D3D4
FCEDEE

Requirements
Must have
• Keep it simply
Nice to have
• Logo and all basic info

```html
<!DOCTYPE html>
<html lang="en">
<head>
<meta charset="utf-8">
<title>Pecan Ridge Paving – Business Card</title>
<link rel="stylesheet" href="https://fonts.googleapis.com/css2?family=Montserrat:wght@800&family=Jost:wght@400;500;600&display=swap">
<style>
  :root {
    --navy: #1f2a5c;
    --red: #b3202f;
    --paper: #ffffff;
    --backdrop: #e4e4e4;
    --ink-soft: #2c3566;
  }
  * { box-sizing: border-box; margin: 0; padding: 0; }
  html, body { width: 1200px; height: 800px; overflow: hidden; }
  body {
    background: var(--backdrop);
    display: flex;
    align-items: center;
    justify-content: center;
    gap: 50px;
    font-family: "Jost", sans-serif;
  }
  .card {
    position: relative;
    width: 525px;
    height: 300px;
    background: var(--paper);
    box-shadow: 0 6px 18px rgba(0,0,0,.12);
    overflow: hidden;
  }

  /* Front */
  .card-front {
    display: flex;
    align-items: center;
    justify-content: center;
  }
  .brand {
    display: flex;
    align-items: center;
    gap: 16px;
  }
  .brand-dot {
    width: 58px; height: 58px;
    border-radius: 50%;
    background: var(--red);
    flex: none;
  }
  .brand-text { display: flex; flex-direction: column; align-items: flex-end; }
  .brand-name {
    font-family: "Montserrat", sans-serif;
    font-weight: 800;
    font-size: 32px;
    line-height: 1;
    color: var(--navy);
    text-transform: uppercase;
    letter-spacing: .5px;
    white-space: nowrap;
  }
  .brand-tagline {
    margin-top: 10px;
    padding-top: 6px;
    border-top: 1.5px solid var(--red);
    width: 220px;
    text-align: right;
    font-size: 13px;
    letter-spacing: 2px;
    color: var(--red);
    font-weight: 500;
    text-transform: uppercase;
    white-space: nowrap;
  }

  /* Back */
  .rule {
    position: absolute;
    height: 2px;
    background: var(--red);
  }
  .rule-top { top: 22px; left: 120px; right: 0; }
  .rule-bottom { bottom: 62px; left: 210px; right: 0; }

  .holder {
    position: absolute;
    top: 48px; right: 34px;
    text-align: right;
  }
  .holder-name {
    font-size: 26px;
    font-weight: 500;
    color: var(--navy);
    letter-spacing: .5px;
    padding-bottom: 6px;
    border-bottom: 1.5px solid var(--red);
    padding-left: 20px;
    white-space: nowrap;
  }
  .holder-title {
    margin-top: 4px;
    font-size: 16px;
    color: var(--red);
    font-weight: 500;
  }

  .contact-list {
    position: absolute;
    top: 128px; right: 30px;
    list-style: none;
    text-align: right;
  }
  .contact-list li {
    display: flex;
    justify-content: flex-end;
    align-items: flex-start;
    gap: 8px;
    font-size: 14px;
    line-height: 1.3;
    color: var(--ink-soft);
    margin-bottom: 6px;
  }
  .contact-list .at { color: var(--red); }
  .contact-list svg { width: 15px; height: 15px; flex: none; margin-top: 2px; }

  .decor-mark {
    position: absolute;
    left: -30px; bottom: 74px;
    width: 170px; height: 170px;
    border-radius: 50%;
    background: var(--navy);
  }

  .website {
    position: absolute;
    left: 34px; bottom: 22px;
    font-size: 22px;
    line-height: 1;
    color: var(--navy);
    letter-spacing: .5px;
  }
  .website .accent { color: var(--red); }
</style>
</head>
<body>

  <section class="card card-front" aria-label="Business card front">
    <div class="brand">
      <span class="brand-dot" aria-hidden="true"></span>
      <div class="brand-text">
        <span class="brand-name">Pecan Ridge Paving</span>
        <span class="brand-tagline">Chip Seal Done Right</span>
      </div>
    </div>
  </section>

  <section class="card card-back" aria-label="Business card back">
    <span class="rule rule-top"></span>
    <span class="rule rule-bottom"></span>

    <div class="holder">
      <p class="holder-name">Dale R. Whitmore</p>
      <p class="holder-title">Director</p>
    </div>

    <ul class="contact-list">
      <li><span>830.555.0173</span>
        <svg viewBox="0 0 16 16" aria-hidden="true"><circle cx="8" cy="8" r="7" fill="none" stroke="var(--red)" stroke-width="1.3"/><path d="M5.5 4.5l1.3 1.3-.8 1a5 5 0 0 0 2.2 2.2l1-.8 1.3 1.3-.9 1a6 6 0 0 1-5-5z" fill="var(--red)"/></svg>
      </li>
      <li><span>Dalewhitmore7<span class="at">@</span>mailbarn.net</span>
        <svg viewBox="0 0 16 16" aria-hidden="true"><circle cx="8" cy="8" r="7" fill="none" stroke="var(--red)" stroke-width="1.3"/><rect x="4.5" y="5.5" width="7" height="5" fill="none" stroke="var(--red)" stroke-width="1.1"/><path d="M4.5 5.5l3.5 2.8 3.5-2.8" fill="none" stroke="var(--red)" stroke-width="1.1"/></svg>
      </li>
      <li><span>Oak Hollow,<br>TX 78099</span>
        <svg viewBox="0 0 16 16" aria-hidden="true"><circle cx="8" cy="8" r="7" fill="none" stroke="var(--red)" stroke-width="1.3"/><path d="M8 12s-3-3-3-5.2a3 3 0 0 1 6 0C11 9 8 12 8 12z" fill="none" stroke="var(--red)" stroke-width="1.1"/><circle cx="8" cy="6.8" r="1" fill="var(--red)"/></svg>
      </li>
    </ul>

    <div class="decor-mark" role="img" aria-label="Pecan Ridge Paving brand mark"></div>

    <p class="website">www.<span class="accent">pecanridgepaving</span>.net</p>
  </section>

</body>
</html>
```